Professional & Modern Technology Business Card

We need a business card for our software/technology firm. Our services include Program/Project Management, Project Controls and Enterprise Analytics. Our clients are usually in the Aviation, Public Works, Transportation and Electric & Water Utility industries. We serve both public and private clients. Would like a very professional, conservative but somewhat modern design. Design, Develop, Deploy is the corporate tagline. We have two offices. The headquarters is in Atlanta, GA and a satellite office In Savannah, GA. Corporate Logo Attached.
Looking to do website and corporate brochure after the successful completion of this project. Would like to begin a working relationship with best designers.
Tagline: Design, Develop, Deploy
Website: www.quelvanesystems.example
My Name: Marla Dunstead
My Title: CEO
Email: mdunstead@quelvanesystems.example
Atlanta Address:
87 Corliss Avenue, #2291
Atlanta, GA 30301
Office: 404.555.0182
Fax: 404.555.0147
Mobile: 404.555.0163
Savannah Address:
350 West Harrow Bend Road
Suite 720
Savannah, GA 31401
Office: 912.555.0139
Fax: 404.555.0147
Mobile: 404.555.0163
Updates
Please include the email address in your designs: mdunstead@quelvanesystems.example.
I appreciate everyone's design efforts. Just a few notes:
1. Please remove the mobile number from the cards
2. The backs of the cards can be utilized for writing notes. Make sure your design on the back of the card is conducive to clearly adding writing if needed.
3. No black backgrounds please
4. Only use the corporate logo on the front of the card. You can use portions of the logo design, but not the logo in totality.
Thank You
Industry/Entity Type
Conservative
Look and feel
Each slider illustrates characteristics of the customer's brand and the style your logo design should communicate.

```html
<!DOCTYPE html>
<html lang="en">
<head>
<meta charset="utf-8">
<title>Quelvane Systems, Inc. – Business Card</title>
<link rel="stylesheet" href="https://fonts.googleapis.com/css2?family=Questrial&family=Montserrat:wght@600&display=swap">
<style>
  :root {
    --backdrop: #1f1f1f;
    --card-white: #ffffff;
    --card-paper: #f7f7f5;
    --band-grey: #ececea;
    --ink-dark: #2a2a2a;
    --ink-mid: #555555;
    --ink-grey: #8a8a8a;
    --accent-yellow: #e8c40f;
  }
  * { box-sizing: border-box; margin: 0; padding: 0; }
  html, body {
    width: 1200px; height: 1000px; overflow: hidden;
    background: var(--backdrop);
    font-family: "Questrial", sans-serif;
  }
  .canvas { position: relative; width: 1200px; height: 1000px; }

  .card {
    position: absolute;
    width: 540px; height: 320px;
    border-radius: 18px;
  }

  /* Front */
  .card-front {
    left: 110px; top: 110px;
    background: var(--card-white);
    clip-path: polygon(70px 0, 100% 0, 100% 100%, 0 100%, 0 70px);
  }
  .brand {
    position: absolute; left: 90px; top: 95px;
    display: flex; align-items: center; gap: 22px;
  }
  .brand-dot {
    width: 58px; height: 58px; border-radius: 50%;
    background: var(--accent-yellow);
  }
  .brand-name {
    color: var(--ink-dark);
    font-size: 40px; line-height: 1.02; letter-spacing: -0.5px;
  }
  .website {
    position: absolute; right: 22px; top: 30px;
    writing-mode: vertical-rl;
    font-size: 13px; letter-spacing: 0.6px;
    color: var(--ink-grey);
  }
  .tagline {
    position: absolute; left: 0; right: 0; bottom: 34px;
    text-align: center;
    font-size: 22px; letter-spacing: 1px;
    color: var(--ink-grey);
  }
  .tagline .sep { margin: 0 10px; }

  /* Back */
  .card-back {
    left: 550px; top: 570px;
    background: var(--card-paper);
    clip-path: polygon(0 0, 100% 0, 100% 100%, 70px 100%, 0 calc(100% - 70px));
    overflow: hidden;
  }
  .name-band {
    position: absolute; left: 0; right: 0; top: 40px; height: 84px;
    background: var(--band-grey);
    border-bottom: 3px solid var(--accent-yellow);
    display: flex; justify-content: space-between; align-items: center;
    padding: 0 26px 0 34px;
  }
  .holder-name {
    font-family: "Montserrat", sans-serif; font-weight: 600;
    font-size: 20px; color: var(--ink-dark);
  }
  .holder-title { font-size: 14px; color: var(--ink-grey); margin-top: 2px; }
  .direct { font-size: 13px; color: var(--ink-dark); line-height: 1.45; }
  .direct .mobile { font-family: "Montserrat", sans-serif; font-weight: 600; }

  .offices {
    position: absolute; left: 34px; right: 26px; top: 152px;
    display: flex; justify-content: space-between;
  }
  .office { width: 190px; font-size: 13px; line-height: 1.5; color: var(--ink-mid); }
  .office-label { color: var(--ink-dark); font-size: 14px; }
  .office-lines { margin-bottom: 8px; }
</style>
</head>
<body>
<main class="canvas">

  <section class="card card-front" aria-label="Card front">
    <div class="brand">
      <span class="brand-dot"></span>
      <div class="brand-name">Quelvane<br>Systems, Inc.</div>
    </div>
    <div class="website">www.quelvanesystems.example</div>
    <p class="tagline">Design<span class="sep">|</span>Develop<span class="sep">|</span>Deploy</p>
  </section>

  <section class="card card-back" aria-label="Card back">
    <div class="name-band">
      <div class="holder">
        <div class="holder-name">Marla Dunstead</div>
        <div class="holder-title">C.E.O</div>
      </div>
      <div class="direct">
        <div class="mobile">404 555 0163</div>
        <div class="email">mdunstead@quelvanesystems.example</div>
      </div>
    </div>

    <div class="offices">
      <div class="office">
        <div class="office-label">Atlanta Address:</div>
        <div class="office-lines">87 Corliss Avenue, #2291<br>Atlanta, GA 30301</div>
        <div>T: 404 555 0182<br>F: 404 555 0147</div>
      </div>
      <div class="office">
        <div class="office-label">Savannah Address:</div>
        <div class="office-lines">350 West Harrow Bend Road<br>Suite 720<br>Savannah, GA 31401</div>
        <div>T: 912 555 0139<br>F: 404 555 0147</div>
      </div>
    </div>
  </section>

</main>
</body>
</html>
```